Vital Spark Electrical in need of a business card design

We need a new business card designed for our electrical business. We have a logo already which I will attach below.
Would like the business card to be..
-BLACK background preferably, possibly white back ground behind logo if colours clash.
-White & Blue (logo blue) text
Something that makes the logo pop, & a modern look. Possibly minimal clean format.

REQUIRE:
-Logo on front & back

TEXT TO INCLUDE (ON ONE SIDE):

Tom Harlow
Director/Electrician
M: 0417 365 208
E:info@vitalsparkelectrical-example.com.au
W:www.vitalsparkelectrical-example.com.au
R.E.C 57318

Custom/New Homes
Renovations
Commercial Office/Shop Fit-outs
Communications & Security Cameras
Electric Vehicle Chargers
Airconditioning
Updates

Requirements
Nice to have
• Possibly even lighten the grey shades for the words 'Vital' & 'Spark' to be more easily read on a black background.

```html
<!DOCTYPE html>
<html lang="en">
<head>
<meta charset="utf-8">
<title>Vital Spark Electrical – Business Card</title>
<link rel="stylesheet" href="https://fonts.googleapis.com/css2?family=Montserrat:wght@800&family=Poppins:wght@500;600&family=Cormorant+Garamond:wght@600&display=swap">
<style>
  :root {
    --page: #ffffff;
    --card: #121212;
    --ring: #1e8fff;
    --ring-light: #6cc8ff;
    --badge: #3fd2f7;
    --badge-text: #10202a;
    --text: #ffffff;
    --brand: #3fc8f0;
  }
  html, body {
    margin: 0;
    width: 1200px;
    height: 720px;
    overflow: hidden;
    background: var(--page);
  }
  .canvas {
    position: relative;
    width: 1200px;
    height: 720px;
  }
  .card-art {
    position: absolute;
    inset: 0;
  }
  .card-content {
    position: absolute;
    left: 0;
    top: 0;
    width: 1152px;
    height: 720px;
    color: var(--text);
    font-family: "Poppins", sans-serif;
  }
  .name {
    position: absolute;
    top: 160px;
    left: 0;
    width: 100%;
    margin: 0;
    text-align: center;
    font-family: "Montserrat", sans-serif;
    font-weight: 800;
    font-size: 58px;
    letter-spacing: 1px;
    line-height: 1;
    text-shadow: 0 0 6px rgba(255,255,255,0.35);
  }
  .name-glow {
    position: absolute;
    top: 222px;
    left: 406px;
    width: 340px;
    height: 3px;
    border-radius: 2px;
    background: linear-gradient(90deg, transparent, var(--ring-light), #ffffff, var(--ring-light), transparent);
    filter: blur(1px);
  }
  .role {
    position: absolute;
    top: 231px;
    left: 421px;
    width: 310px;
    height: 41px;
    border-radius: 5px;
    background: var(--badge);
    color: var(--badge-text);
    font-family: "Cormorant Garamond", serif;
    font-weight: 600;
    font-size: 28px;
    line-height: 41px;
    text-align: center;
  }
  .contact {
    position: absolute;
    left: 0;
    width: 100%;
    display: flex;
    justify-content: center;
    align-items: center;
    gap: 10px;
    font-weight: 500;
    font-size: 21px;
    line-height: 1;
  }
  .contact svg { flex: none; }
  .contact.phone { top: 336px; font-size: 26px; gap: 16px; }
  .contact.email { top: 378px; }
  .contact.web   { top: 425px; }
  .licence {
    position: absolute;
    top: 474px;
    left: 0;
    width: 100%;
    text-align: center;
    font-weight: 500;
    font-size: 22px;
    line-height: 1;
  }
  .brand {
    position: absolute;
    top: 560px;
    left: 0;
    width: 100%;
    display: flex;
    justify-content: center;
    align-items: center;
    gap: 14px;
    color: var(--brand);
    font-family: "Poppins", sans-serif;
    font-weight: 600;
    font-size: 30px;
    line-height: 1;
  }
  .brand-mark {
    width: 30px;
    height: 30px;
    background: var(--brand);
    border-radius: 3px;
  }
</style>
</head>
<body>
<div class="canvas">
  <svg class="card-art" width="1200" height="720" viewBox="0 0 1200 720" aria-hidden="true">
    <defs>
      <clipPath id="card-shape">
        <rect x="19" y="32" width="1160" height="658" rx="95"/>
      </clipPath>
      <radialGradient id="inner-fill" cx="50%" cy="25%" r="75%">
        <stop offset="0" stop-color="#1c1c1c"/>
        <stop offset="0.6" stop-color="#2a2a2a"/>
        <stop offset="1" stop-color="#4a4a4a"/>
      </radialGradient>
      <filter id="soft-glow" x="-20%" y="-20%" width="140%" height="140%">
        <feGaussianBlur stdDeviation="14"/>
      </filter>
      <filter id="tight-glow" x="-20%" y="-20%" width="140%" height="140%">
        <feGaussianBlur stdDeviation="4"/>
      </filter>
      <filter id="spark-blur" x="-100%" y="-100%" width="300%" height="300%">
        <feGaussianBlur stdDeviation="3"/>
      </filter>
    </defs>
    <g class="card" clip-path="url(#card-shape)">
      <rect class="card-base" x="19" y="32" width="1160" height="658" fill="var(--card)"/>
      <circle class="ring-inner" cx="576" cy="357" r="350" fill="url(#inner-fill)"/>
      <circle class="ring-halo" cx="576" cy="357" r="354" fill="none" stroke="var(--ring)" stroke-width="34" filter="url(#soft-glow)" opacity="0.9"/>
      <circle class="ring-glow" cx="576" cy="357" r="354" fill="none" stroke="var(--ring-light)" stroke-width="10" filter="url(#tight-glow)"/>
      <circle class="ring-line" cx="576" cy="357" r="354" fill="none" stroke="#bfe6ff" stroke-width="3"/>
      <g class="ring-sparks" fill="#ffffff" filter="url(#spark-blur)">
        <circle cx="277" cy="172" r="6"/>
        <circle cx="226" cy="357" r="6"/>
        <circle cx="300" cy="560" r="5"/>
        <circle cx="790" cy="80" r="6"/>
        <circle cx="926" cy="340" r="6"/>
        <circle cx="860" cy="560" r="5"/>
        <circle cx="576" cy="700" r="5"/>
      </g>
    </g>
  </svg>

  <div class="card-content">
    <h1 class="name">TOM HARLOW</h1>
    <div class="name-glow"></div>
    <div class="role">Director/Electrician</div>

    <div class="contact phone">
      <svg width="34" height="22" viewBox="0 0 34 22" aria-hidden="true">
        <path d="M4 3c3-2 6-2 8 0l2 3-3 3c1 3 3 5 6 6l3-3 3 2c2 2 2 5 0 7-4 2-10 0-15-5S2 6 4 3z" fill="#ffffff" transform="scale(1.05) translate(0 -2)"/>
        <path d="M24 3a8 8 0 0 1 6 6M24 7a4 4 0 0 1 3 3" stroke="#ffffff" stroke-width="2" fill="none" stroke-linecap="round"/>
      </svg>
      <span>0417 365 208</span>
    </div>

    <div class="contact email">
      <svg width="30" height="24" viewBox="0 0 30 24" aria-hidden="true">
        <rect x="2" y="5" width="26" height="17" rx="2" fill="none" stroke="#ffffff" stroke-width="2"/>
        <path d="M2 6l13 9 13-9" fill="none" stroke="#ffffff" stroke-width="2"/>
        <circle cx="15" cy="6" r="4.5" fill="#ffffff"/>
      </svg>
      <span>info@vitalsparkelectrical-example.com.au</span>
    </div>

    <div class="contact web">
      <svg width="28" height="28" viewBox="0 0 28 28" aria-hidden="true">
        <g fill="none" stroke="#ffffff" stroke-width="1.8">
          <circle cx="14" cy="14" r="12"/>
          <ellipse cx="14" cy="14" rx="5.5" ry="12"/>
          <path d="M2 14h24M4 8h20M4 20h20"/>
        </g>
      </svg>
      <span>www.vitalsparkelectrical-example.com.au</span>
    </div>

    <div class="licence">R.E.C 57318</div>

    <div class="brand">
      <span class="brand-mark"></span>
      <span class="brand-name">Vital Spark Electrical</span>
    </div>
  </div>
</div>
</body>
</html>
```